"Copper Horizons" poster for feature film

I need a poster for my first narrative feature film. Genre: Drama/Comedy. Synopsis: After going through a break up and moving back home, Tobias struggles through a "quarter life crisis" in pursuit of his dream of making a feature film. Tobias wants to tell a compassionate story about mental illness and its effects on a family, but the lines between fiction and reality are blurred, challenging the bond between two brothers.

Target Market(s)

Film Festivals, Prospective viewers on Vidorly/Quorvia.

Industry/Entity Type

Film Production

Other font styles liked:
• Birch STD

Colors
faa54b
f78f20
85abd2
3176b5
0355a3
fac994
f9ba93
f37122
fece3e

Requirements
Must have
• Title: Copper Horizons
• Minimalist approach.
• Please look at reference posters/prototypes.
Nice to have
• -the idea of contrasting the two brothers and the struggle of living with a mental illness.
• -the setting of the film is in Arizona, desert, living back at home as an adult.
• -the struggle of a writer. A film about a film.
• 5 phases of "The Quarter Life Crisis"
• 1. You feel trapped by your life choices, like your job, relationship, or both. You’re living on “autopilot.”
• 2. You get a sense of “I’ve got to get out of this” and feel a growing sense that change is possible if you just take a leap.
• 3. You quit the job, end the relationship, or break the commitment that’s making you feel trapped. Then you detach and enter a “time out” period where try to rediscover who you are and who you want to be.
• 4. You begin rebuilding your life slowly but surely.
• 5. You develop new commitments that are more in line with your interests and aspirations.

```html
<!DOCTYPE html>
<html lang="en">
<head>
<meta charset="utf-8">
<title>Copper Horizons — Poster</title>
<link rel="stylesheet" href="https://fonts.googleapis.com/css2?family=Amatic+SC:wght@400;700&display=swap">
<style>
  :root {
    --paper: #ffffff;
    --horizon-blue: #0355a3;
    --sky-blue: #3176b5;
    --copper: #f37122;
    --amber: #f78f20;
    --sand: #faa54b;
  }
  html, body {
    margin: 0;
    padding: 0;
    width: 849px;
    height: 1200px;
    overflow: hidden;
    background: var(--paper);
  }
  .poster {
    position: relative;
    width: 849px;
    height: 1200px;
    overflow: hidden;
    background: var(--paper);
  }
  .hero-band {
    position: absolute;
    inset: 0;
    display: block;
  }
  .title {
    position: absolute;
    right: 45px;
    top: 872px;
    margin: 0;
    text-align: right;
    font-family: "Amatic SC", sans-serif;
    font-weight: 400;
    font-size: 146px;
    line-height: 0.78;
    letter-spacing: 1px;
  }
  .title-line { display: block; }
  .title-top { color: var(--horizon-blue); }
  .title-bottom { color: var(--copper); }
</style>
</head>
<body>
<main class="poster">
  <svg class="hero-band" width="849" height="1200" viewBox="0 0 849 1200" role="img" aria-label="Diagonal illustration of a laptop keyboard, keys shading from blue to copper orange">
    <defs>
      <linearGradient id="band-fill" x1="0" y1="0.35" x2="0.75" y2="0.55">
        <stop offset="0" stop-color="var(--horizon-blue)"/>
        <stop offset="0.38" stop-color="var(--sky-blue)"/>
        <stop offset="0.5" stop-color="var(--amber)"/>
        <stop offset="1" stop-color="var(--copper)"/>
      </linearGradient>
    </defs>
    <polygon points="0,350 522,0 849,0 849,489 0,1060" fill="url(#band-fill)"/>
  </svg>

  <h1 class="title">
    <span class="title-line title-top">COPPER</span>
    <span class="title-line title-bottom">HORIZONS</span>
  </h1>
</main>
</body>
</html>
```